Flenzo Thumbnail for Educational Video About KR9

Please design a bespoke thumbnail for a Flenzo video with the following title:
"Nobody Expected What Came Over That Ridge"
The video is about the battle for Castle Brunok, which was a small battle that happened during KR9, in which the Germans fought against themselves for control of Castle Brunok.
The thumbnail should be 1920x1080 pixels

```html
<!DOCTYPE html>
<html lang="en">
<head>
<meta charset="utf-8">
<title>Flenzo Thumbnail – Nobody Expected What Came Over That Ridge</title>
<link rel="stylesheet" href="https://fonts.googleapis.com/css2?family=Cinzel:wght@700;900&display=swap">
<style>
  :root {
    --sky-light: #eef0f2;
    --smoke-violet: #6e6478;
    --storm-dark: #1c1a20;
    --ground-black: #050505;
    --title-shadow: #0a0a0a;
    --rule-white: #f4f1ee;
  }
  * { margin: 0; padding: 0; box-sizing: border-box; }
  html, body {
    width: 1200px;
    height: 675px;
    overflow: hidden;
    background: var(--ground-black);
  }
  .thumbnail {
    position: relative;
    width: 1200px;
    height: 675px;
    overflow: hidden;
  }
  .battle-scene {
    position: absolute;
    inset: 0;
    background:
      radial-gradient(ellipse 38% 45% at 8% 22%, var(--sky-light) 0%, rgba(238,240,242,0) 70%),
      radial-gradient(ellipse 30% 30% at 30% 55%, rgba(220,218,226,0.75) 0%, rgba(220,218,226,0) 70%),
      radial-gradient(ellipse 55% 40% at 28% 30%, var(--smoke-violet) 0%, rgba(110,100,120,0) 75%),
      radial-gradient(ellipse 60% 50% at 75% 30%, #2a2730 0%, rgba(42,39,48,0) 80%),
      linear-gradient(180deg, #4a4550 0%, var(--storm-dark) 55%, var(--ground-black) 85%);
  }
  .headline {
    position: absolute;
    inset: 0;
    width: 1200px;
    height: 675px;
  }
  .headline text {
    font-family: "Cinzel", "Times New Roman", serif;
    font-weight: 900;
  }
  .headline .shadow { fill: var(--title-shadow); }
  .headline .fill-red { fill: url(#red-speckle); }
  .headline .fill-white { fill: url(#white-speckle); }
  .headline .fill-plain { fill: var(--rule-white); }
  .headline .rule { stroke: var(--rule-white); stroke-width: 1.5; }
</style>
</head>
<body>
<main class="thumbnail">
  <div class="battle-scene" role="img" aria-label="Painted battlefield: a hooded soldier with a rifle runs through smoke past fallen branches while silhouetted troops advance behind him"></div>

  <svg class="headline" viewBox="0 0 1200 675" aria-label="Nobody Expected What Came Over That Ridge">
    <defs>
      <linearGradient id="red-speckle" x1="0" y1="0" x2="1" y2="1">
        <stop offset="0" stop-color="#d6474a"/>
        <stop offset="0.35" stop-color="#c8383c"/>
        <stop offset="0.5" stop-color="#e7a9a8"/>
        <stop offset="0.65" stop-color="#c8383c"/>
        <stop offset="1" stop-color="#b93035"/>
      </linearGradient>
      <linearGradient id="white-speckle" x1="0" y1="0" x2="1" y2="0">
        <stop offset="0" stop-color="#f4f1ee"/>
        <stop offset="0.4" stop-color="#e6c9c7"/>
        <stop offset="0.6" stop-color="#cf5a5b"/>
        <stop offset="1" stop-color="#c8383c"/>
      </linearGradient>
    </defs>

    <g class="line-one">
      <text class="shadow" x="539" y="310" font-size="62" textLength="262" lengthAdjust="spacingAndGlyphs">NOBODY</text>
      <text class="fill-red" x="534" y="304" font-size="62" textLength="262" lengthAdjust="spacingAndGlyphs">NOBODY</text>
    </g>

    <g class="line-two">
      <text class="shadow" x="541" y="391" font-size="80" textLength="360" lengthAdjust="spacingAndGlyphs">EXPECTED</text>
      <text class="fill-white" x="536" y="385" font-size="80" textLength="360" lengthAdjust="spacingAndGlyphs">EXPECTED</text>
    </g>

    <g class="line-three">
      <text class="shadow" x="463" y="485" font-size="112" textLength="628" lengthAdjust="spacingAndGlyphs">WHAT CAME</text>
      <text class="fill-white" x="458" y="479" font-size="112" textLength="628" lengthAdjust="spacingAndGlyphs">WHAT CAME</text>
    </g>

    <g class="line-four">
      <line class="rule" x1="325" y1="514" x2="684" y2="514"/>
      <line class="rule" x1="772" y1="514" x2="1131" y2="514"/>
      <text class="fill-plain" x="692" y="530" font-size="32" textLength="72" lengthAdjust="spacingAndGlyphs">OVER</text>
    </g>

    <g class="line-five">
      <text class="fill-red" x="325" y="616" font-size="96" textLength="806" lengthAdjust="spacingAndGlyphs">THAT RIDGE</text>
    </g>
  </svg>
</main>
</body>
</html>
```